BRWK branding
Stationery & misc. Design Elements
Thank Delphine!
To all designers: My client has chosen Orvo Design as the winner on this project. Thanks to all for the hard work and revised designs. Keep an eye out for another project for Birchwood Spinal Care Logo. Thanks for the efforts.
Delphine
@ Brambly : I think some of your winning designs(concept) are similar....
So,are these copied from others???
No,Dear Friend,Everything is separate from others as like as me.
Don't be upset... :)
Wishing you all the best.
-A Friend,
OrvoDesigner
http://www.draftvane.example/drafts/display/contest/10001/draft/300001
http://www.draftvane.example/drafts/display/contest/10002/draft/300002
http://www.draftvane.example/drafts/display/contest/10003/draft/300003
http://www.draftvane.example/drafts/display/contest/10004/draft/300004
http://www.draftvane.example/drafts/display/contest/10005/draft/300005
http://www.draftvane.example/drafts/display/contest/10006/draft/300006
http://www.draftvane.example/drafts/display/contest/10007/draft/300007
@ Dear Brambly : Yes,I already won that contest. I think - you guess something similar like that. Would you compare again ,please? It is not copied from that.Please,See carefully Envelope and the Letterhead again(that you thinking).
Only the color format are similar that I like most.Without this everything is different(about the color code,Color area,address position,watermark,line and the logo position).Is it clear,dear?
Thanks for your hard trying about the design.
I really wish your success.
(A Competitor and a friend.)
-OrvoDesigner
Orvo Design,
u already winning this design
To all designers: remember to submit a page or so of additional design elements for use in future marketing collateral - as stated in
the project brief. Thanks
Correction ** New logo uploaded 11/15
Please upload ai or eps of your logo.

```html
<!DOCTYPE html>
<html lang="en">
<head>
<meta charset="utf-8">
<title>BRWK business cards</title>
<link href="https://fonts.googleapis.com/css2?family=Open+Sans:wght@400;600;700&display=swap" rel="stylesheet">
<style>
  :root {
    --backdrop: #e4e6e8;
    --paper: #ffffff;
    --paper-shade: #f1f2f4;
    --brand-blue: #1f6fb8;
    --brand-blue-deep: #14508c;
    --brand-blue-light: #3f8fd4;
    --ink: #1f5f9e;
    --ink-muted: #4a6a8a;
    --ink-soft: #5d6d7c;
  }
  * { box-sizing: border-box; margin: 0; padding: 0; }
  html, body { width: 1200px; height: 871px; overflow: hidden; }
  body {
    background: var(--backdrop);
    font-family: "Open Sans", Arial, sans-serif;
    position: relative;
  }
  .card {
    position: absolute;
    top: 292px;
    width: 500px;
    height: 286px;
    border-radius: 20px;
    overflow: hidden;
    box-shadow: 0 10px 28px rgba(0,0,0,0.22);
  }
  .card--front { left: 70px; background: linear-gradient(135deg, var(--paper) 0%, var(--paper) 60%, var(--paper-shade) 100%); }
  .card--back { left: 630px; background: radial-gradient(circle at 30% 20%, var(--brand-blue-light) 0%, var(--brand-blue) 45%, var(--brand-blue-deep) 100%); }

  .card__name {
    position: absolute; left: 250px; top: 82px;
    font-size: 25px; font-weight: 700; color: var(--ink); letter-spacing: 0.2px;
  }
  .card__title {
    position: absolute; left: 252px; top: 116px;
    font-size: 12px; font-weight: 400; color: var(--ink-muted);
  }
  .card--back .card__name { color: #ffffff; }
  .card--back .card__title { color: #dbe9f7; }

  .brand {
    position: absolute; left: 34px; top: 128px;
    display: flex; align-items: center; gap: 7px;
  }
  .brand__dot { width: 12px; height: 12px; border-radius: 50%; background: var(--brand-blue); }
  .brand__name { font-size: 16px; font-weight: 700; color: var(--brand-blue); letter-spacing: 1px; }
  .card--back .brand__dot { background: #ffffff; }
  .card--back .brand__name { color: #ffffff; }

  .contact {
    position: absolute; left: 34px; top: 194px;
    font-size: 9px; line-height: 12.5px; color: var(--ink-soft);
    list-style: none;
  }
  .card--back .contact { color: #e6f0fa; }

  .accent-bar {
    position: absolute; left: 0; top: 196px; width: 7px; height: 64px;
    background: var(--brand-blue);
  }
  .card--back .accent-bar { background: #ffffff; }
</style>
</head>
<body>

<article class="card card--front">
  <h1 class="card__name">Marren Osk, M.D.</h1>
  <p class="card__title">Birchwood Spinal Care</p>
  <div class="brand"><span class="brand__dot"></span><span class="brand__name">BRWK</span></div>
  <span class="accent-bar"></span>
  <ul class="contact">
    <li>218 Harlow Avenue</li>
    <li>Fenwick, NJ 07990</li>
    <li>P: 555-010-2040</li>
    <li>F: 555-010-2041</li>
    <li>C: 555-010-2042</li>
    <li>E: m.osk@birchwoodspine.example</li>
  </ul>
</article>

<article class="card card--back">
  <h1 class="card__name">Marren Osk, M.D.</h1>
  <p class="card__title">Birchwood Spinal Care</p>
  <div class="brand"><span class="brand__dot"></span><span class="brand__name">BRWK</span></div>
  <span class="accent-bar"></span>
  <ul class="contact">
    <li>218 Harlow Avenue</li>
    <li>Fenwick, NJ 07990</li>
    <li>P: 555-010-2040</li>
    <li>F: 555-010-2041</li>
    <li>C: 555-010-2042</li>
    <li>E: m.osk@birchwoodspine.example</li>
  </ul>
</article>

</body>
</html>
```